Flyer for Compassion training days

I need a A5-size, single-sided flyer design for my training days. They are weekends in a blend of Compassionate Communication and Buddhist teachings called Palomere Communication. The logo for Palomere that should be included.
The flyer needs room for 1) course title, 2) course dates, location & price, 3) course description, 4) booking info, 5) my picture & short bio, and 6) the palomere.co website (yes, it is 'co' and not 'com).
Updates

Target Market(s)

Women 35-65 years, well-educated, spiritually minded. May have interests like yoga and meditation.

Industry/Entity Type

Health And Wellness

Font styles to use
Sans Serif
Other font styles liked:
• Blue Plaque, Josefina are both great

Colors
fbf289
fdf9cf
cfeae6
33b8a4

Requirements
Must have
• The Palomere logo; my picture.
• Elegance. Calm and expansive feel.
• The poster provided in the project files shows you the kind of information I need to include.
• Colours -- greens and yellows, but the options on pixel harbor are not quite the right shades.
• The logo colour can be changed.
Nice to have
• Classy (but not cliche) image associated with Buddhism; gentle curves similar to those on the business card (see project files).
Should not have
• Dark background. Busy, loud design. Overly 'swirly' design. Images that I have to buy separately.

```html
<!DOCTYPE html>
<html lang="en">
<head>
<meta charset="utf-8">
<title>Palomere Communication Core Course</title>
<link href="https://fonts.googleapis.com/css2?family=Open+Sans:wght@300;400;600&display=swap" rel="stylesheet">
<style>
  :root {
    --cream: #fdf9cf;
    --butter: #fbf289;
    --mist: #cfeae6;
    --jade: #33b8a4;
    --jade-deep: #1f7c6f;
    --ink: #24564f;
    --ink-soft: #3a6b63;
  }
  html, body {
    margin: 0;
    padding: 0;
    width: 1200px;
    height: 851px;
    overflow: hidden;
  }
  .flyer {
    position: relative;
    width: 1200px;
    height: 851px;
    overflow: hidden;
    background: linear-gradient(135deg, var(--cream) 0%, #f6f7de 45%, var(--mist) 100%);
    font-family: "Open Sans", sans-serif;
    font-weight: 300;
    color: var(--ink);
  }
  .art {
    position: absolute;
    display: block;
  }
  .art-lotus { left: 0; top: 178px; width: 455px; height: 200px; }
  .art-ornament { left: 0; top: 470px; width: 560px; height: 381px; }
  .art-figure { left: 0; top: 600px; width: 175px; height: 251px; }
  .portrait { left: 212px; top: 636px; width: 150px; height: 150px; }

  .brand {
    position: absolute;
    left: 384px;
    top: 690px;
    display: flex;
    align-items: center;
    gap: 12px;
    margin: 0;
    font-size: 28px;
    line-height: 36px;
    font-weight: 400;
    color: var(--jade-deep);
  }
  .brand-dot {
    width: 22px;
    height: 22px;
    border-radius: 50%;
    background: var(--jade);
  }

  .tagline {
    position: absolute;
    left: 38px;
    top: 44px;
    margin: 0;
    font-size: 29px;
    line-height: 38px;
    font-weight: 400;
    color: var(--jade-deep);
  }
  .course {
    position: absolute;
    left: 206px;
    top: 366px;
  }
  .course-title {
    margin: 0 0 34px;
    font-size: 31px;
    line-height: 38px;
    font-weight: 400;
    color: var(--jade-deep);
  }
  .course-details {
    margin: 0;
    font-size: 29px;
    line-height: 38px;
    font-weight: 400;
    color: var(--ink);
  }
  .info {
    position: absolute;
    left: 627px;
    top: 38px;
    width: 560px;
    font-size: 18.4px;
    line-height: 23.4px;
    color: var(--ink-soft);
  }
  .info p { margin: 0 0 23.4px; }
  .info .lead-in { margin-bottom: 0; }
  .info ul {
    list-style: none;
    margin: 0 0 23.4px;
    padding: 0 0 0 12px;
  }
  .info li { padding-left: 12px; text-indent: -12px; }
  .info li::before { content: "* "; color: var(--jade); }
  .facilitator {
    display: grid;
    grid-template-columns: 108px 1fr;
  }
  .booking {
    display: grid;
    grid-template-columns: 86px 1fr;
  }
  .website {
    position: absolute;
    right: 34px;
    top: 794px;
    margin: 0;
    font-size: 29px;
    line-height: 36px;
    font-weight: 400;
    color: var(--jade-deep);
  }
</style>
</head>
<body>
<main class="flyer">
  <svg class="art art-lotus" viewBox="0 0 455 200" role="img" aria-label="Line illustration of lotus flowers and lily pads floating on water">
    <defs>
      <radialGradient id="lotusFill" cx="0.4" cy="0.5" r="0.6">
        <stop offset="0" stop-color="#33b8a4" stop-opacity="0.35"/>
        <stop offset="1" stop-color="#cfeae6" stop-opacity="0"/>
      </radialGradient>
    </defs>
    <ellipse cx="210" cy="100" rx="245" ry="100" fill="url(#lotusFill)"/>
  </svg>

  <svg class="art art-ornament" viewBox="0 0 560 381" role="img" aria-label="Faint decorative circle and paisley ornament pattern">
    <defs>
      <radialGradient id="ornamentFill" cx="0.25" cy="0.45" r="0.7">
        <stop offset="0" stop-color="#fbf289" stop-opacity="0.55"/>
        <stop offset="1" stop-color="#fbf289" stop-opacity="0"/>
      </radialGradient>
    </defs>
    <rect width="560" height="381" fill="url(#ornamentFill)"/>
  </svg>

  <svg class="art art-figure" viewBox="0 0 175 251" role="img" aria-label="Pale stone statue of a seated Buddha in meditation">
    <defs>
      <linearGradient id="figureFill" x1="0" y1="0" x2="0" y2="1">
        <stop offset="0" stop-color="#cfeae6"/>
        <stop offset="1" stop-color="#8fd3c7"/>
      </linearGradient>
    </defs>
    <path d="M0 251 V70 Q0 0 87 0 Q175 0 175 90 V251 Z" fill="url(#figureFill)"/>
  </svg>

  <svg class="art portrait" viewBox="0 0 150 150" role="img" aria-label="Portrait photograph of facilitator Maribeth Lindqvist">
    <circle cx="75" cy="75" r="73" fill="#cfeae6" stroke="#33b8a4" stroke-width="3"/>
  </svg>

  <p class="brand"><span class="brand-dot"></span>Palomere</p>

  <h2 class="tagline">Mindfullness + Kindness +<br>Compassionate Communication=</h2>

  <section class="course">
    <h1 class="course-title">Palomere Communication<br>Core Course</h1>
    <p class="course-details">11-12 Dec<br>Thornbury Centre, Edinburgh<br>£125/100</p>
  </section>

  <section class="info">
    <p>Palomere Communication can help you<br>increase awareness &amp; compassion in<br>everyday speech (with yourself &amp; others),<br>better understand your own patterns,<br>and build resilience to challenging situations.</p>
    <p>Choose from:</p>
    <p class="lead-in">In this 2-day Core Course, we’ll explore:</p>
    <ul>
      <li>Compassionate Communication;</li>
      <li>Buddhist teachings on Right Speech,<br>loving-kindness, Right Effort, and more;</li>
      <li>mindfulness practices;</li>
      <li>choices available to us in our everyday speech.</li>
    </ul>
    <p class="facilitator"><span>Facilitator:</span><span>Maribeth Lindqvist<br>is an experienced group facilitator,<br>having worked with a range of organisations and<br>presented at a number of festivals &amp; conferences.</span></p>
    <p>Maribeth offers coaching in Palomere Communication.</p>
    <p>This workshop will be of interest if<br>you’d like to improve personal and/or<br>professional relationships.<br>Open to all, best suited to those<br>with at least 1 year’s experience<br>with Mindfulness,&nbsp; Buddhism,<br>&nbsp;or Compassionate Communication / NVC.</p>
    <p class="booking"><span>Booking:</span><span>Book online at Ticketvale<br>or write maribeth@palomere.co</span></p>
  </section>

  <p class="website">www.palomere.co</p>
</main>
</body>
</html>
```